A book main title will be, "Kindle Your Clients"
The subtext will be, "Launch your offer with a tale that crackles"
Would like it to blend with my web site brand. You can find it here: www.kindleyourclients.example

Audience is business and revenue leaders for small, medium and large businesses. They have a new solution, or want to enter a new market, and they need to "inspire their buyers" meaning getting the buyers to want to change enough to overcome their status quo bias. They need a story that sizzles to do this.

```html
<!DOCTYPE html>
<html lang="en">
<head>
<meta charset="utf-8">
<title>Kindle Your Clients — Book Cover</title>
<link rel="stylesheet" href="https://fonts.googleapis.com/css2?family=Montserrat:wght@500;700;800&display=swap">
<style>
  :root {
    --page-bg: #dedbcc;
    --teal: #1aaa9f;
    --teal-deep: #139488;
    --mist-teal: #cfe6e4;
    --ink: #2b2b2d;
    --white: #ffffff;
  }
  html, body {
    margin: 0;
    padding: 0;
    width: 1200px;
    height: 800px;
    overflow: hidden;
    background: var(--page-bg);
  }
  .book-cover {
    position: absolute;
    left: 320px;
    top: 0;
    width: 560px;
    height: 800px;
    overflow: hidden;
    font-family: "Montserrat", Arial, sans-serif;
  }
  .cover-art {
    position: absolute;
    inset: 0;
    width: 560px;
    height: 800px;
    display: block;
  }
  .cover-title {
    position: absolute;
    left: 0;
    right: 0;
    top: 92px;
    margin: 0;
    text-align: center;
    line-height: 1;
  }
  .cover-title__lead {
    display: block;
    font-weight: 800;
    font-size: 80px;
    letter-spacing: 1px;
    color: var(--teal);
  }
  .cover-title__rest {
    display: block;
    margin-top: 6px;
    font-weight: 700;
    font-size: 64px;
    color: var(--ink);
  }
  .cover-subtitle {
    position: absolute;
    left: 0;
    right: 0;
    top: 382px;
    margin: 0;
    text-align: center;
    font-weight: 500;
    font-size: 28px;
    line-height: 1.25;
    letter-spacing: 0.5px;
    color: var(--white);
    transform: rotate(-9deg);
  }
</style>
</head>
<body>
  <main class="book-cover">
    <svg class="cover-art" viewBox="0 0 560 800" xmlns="http://www.w3.org/2000/svg">
      <defs>
        <linearGradient id="sky-fill" x1="0" y1="0" x2="1" y2="1">
          <stop offset="0" stop-color="#8fa9a8"/>
          <stop offset="0.3" stop-color="#e8f1f1"/>
          <stop offset="0.65" stop-color="#e2eeed"/>
          <stop offset="1" stop-color="#6fb8ae"/>
        </linearGradient>
        <linearGradient id="ground-fill" x1="0" y1="0" x2="1" y2="1">
          <stop offset="0" stop-color="#93d6cb"/>
          <stop offset="0.35" stop-color="#a4ccc8"/>
          <stop offset="0.55" stop-color="#4fae9d"/>
          <stop offset="0.72" stop-color="#a6d3cf"/>
          <stop offset="1" stop-color="#b2dcdc"/>
        </linearGradient>
      </defs>

      <rect class="cover-art__sky" x="0" y="0" width="560" height="340" fill="url(#sky-fill)"
            role="img" aria-label="Abstract backdrop of soft teal glass towers and light"/>

      <rect class="cover-art__scene" x="0" y="420" width="560" height="380" fill="url(#ground-fill)"
            role="img" aria-label="Illustration of mint stepped platforms split by a deep teal gap, with a speaker holding a megaphone addressing a distant listener"/>

      <path class="cover-art__band"
            d="M0 272 L108 340 Q120 347 134 344 L560 268 L560 484 L138 553 Q124 556 110 549 L0 490 Z"
            fill="var(--teal)"/>
      <path class="cover-art__band-edge"
            d="M0 272 L108 340 Q120 347 134 344 L560 268"
            fill="none" stroke="var(--mist-teal)" stroke-width="5"/>
    </svg>

    <h1 class="cover-title">
      <span class="cover-title__lead">KINDLE</span>
      <span class="cover-title__rest">Your Clients</span>
    </h1>

    <p class="cover-subtitle">Launch your offer with a<br>tale that crackles</p>
  </main>
</body>
</html>
```